Meadow Lark Roasters (coffee packaging design)

Project Overview:
🔥 Attention for Designer

You have been provided with detailed brand files, fonts, and reference designs for a reason. I expect work that is better than what I could create myself. The design should be thoughtful, professional, and aligned with our brand identity.

Read the full project description carefully. Every detail matters. If something is unclear, ask questions before starting. Do not just drop logos or assets onto a layout. Understand the intent and build something that fits the vision.

Rushed or mediocre work will not be accepted. I want quality over quantity with real creative thinking and brand awareness behind it.
We’re creating a high-end yet playful packaging design for Meadow Lark Roasters, intended to reflect the classy and nature-inspired feel of Pine Hollow(pinehollowyardplay.example) while adding a touch of lighthearted charm.

Design Elements to Include

Logo & Brand Cues: Incorporate the Pine Hollow logo (round circle with dog head) and use our established color palette and leafy, forestry brand patterns. This will ensure consistency and a high-end feel.

Doodle Elements (Optional): If it suits the design, feel free to incorporate the doodle-style handwriting and sketches that appear on our website (like dog names or playful notes). This adds a personal and approachable touch, though it’s not mandatory.

Bag Format: Design for a 16 oz bag, with the option to either do a full custom print or a high-quality branded sticker on a neutral bag. The goal is to make the packaging feel special and on-brand.

Overall Vibe
Think modern, classy, and a little bit whimsical. The packaging should look polished enough to be a premium product while still capturing the fun, dog-friendly personality of Pine Hollow.
Needs: its own special logo something that can be put on cups, and stickers. We also want the bag design to feel special and not just a logo slapped onto a coffee bag, so in a way i want 2 deliverables.

fonts: in the files uploaded

Target Market(s)

Dog Owners

Font styles to use
Other font styles liked:
• Fonts are in files

Requirements
Must have
• Use our brand guidelines

```html
<!DOCTYPE html>
<html lang="en">
<head>
<meta charset="UTF-8">
<title>Meadow Lark Roasters – Medium Roast 16 oz</title>
<link rel="stylesheet" href="https://fonts.googleapis.com/css2?family=Barlow:wght@400;500;800;900&display=swap">
<style>
  :root {
    --backdrop: #cbcbcb;
    --forest: #2f4a16;
    --forest-leaf: #3f5e1f;
    --cream: #e6cd8e;
    --tan: #d8bd86;
    --tan-soft: #e4d3ab;
    --paper: #f1f1ee;
    --paper-leaf: #e3e6d4;
    --lime: #c2cc26;
    --roast: #6b4a30;
  }
  * { box-sizing: border-box; margin: 0; padding: 0; }
  html, body {
    width: 1200px; height: 900px; overflow: hidden;
    background: var(--backdrop);
    font-family: "Barlow", Arial, sans-serif;
  }
  .package-front {
    position: absolute; left: 390px; top: 120px;
    width: 420px; height: 660px;
    border-radius: 6px; overflow: hidden;
    background: var(--paper);
  }
  .panel-fill { position: absolute; inset: 0; width: 100%; height: 100%; }
  .brand-mark {
    position: absolute; left: 166px; top: 46px;
    width: 88px; height: 88px; border-radius: 50%;
    background: var(--cream);
  }
  .brand-name {
    position: absolute; left: 0; right: 0; top: 160px;
    text-align: center; color: var(--cream);
    font-weight: 900; font-size: 52px; line-height: 1;
    letter-spacing: 0.5px; text-transform: uppercase;
  }
  .quality-seal {
    position: absolute; left: 180px; top: 274px;
    width: 116px; height: 106px;
  }
  .quality-seal svg { position: absolute; inset: 0; }
  .quality-seal .seal-text {
    position: absolute; inset: 0;
    display: flex; align-items: center; justify-content: center;
    text-align: center; color: var(--forest);
    font-weight: 500; font-size: 15px; line-height: 1.1;
    text-transform: uppercase; letter-spacing: 0.5px;
  }
  .mascot-art {
    position: absolute; left: 120px; top: 400px;
    width: 230px; height: 236px; border-radius: 60px 60px 18px 18px;
    background:
      radial-gradient(ellipse 55% 40% at 62% 78%, rgba(107,74,48,0.55) 0%, rgba(107,74,48,0) 100%),
      radial-gradient(ellipse 60% 50% at 40% 35%, var(--tan) 0%, rgba(216,189,134,0) 100%),
      var(--tan-soft);
    opacity: 0.85;
  }
  .roast-badge {
    position: absolute; left: 18px; top: 560px;
    width: 94px; height: 94px; border-radius: 50%;
    background: var(--forest); border: 3px solid var(--paper);
    box-shadow: 0 0 0 2px var(--forest);
    display: flex; flex-direction: column; align-items: center; justify-content: center;
    transform: rotate(-14deg);
    font-weight: 900; text-transform: uppercase; line-height: 0.95;
  }
  .roast-badge .roast-level { color: var(--cream); font-size: 17px; }
  .roast-badge .roast-word { color: var(--paper); font-size: 22px; }
  .roast-badge .star { color: var(--paper); font-size: 8px; line-height: 1.2; }
  .net-weight {
    position: absolute; right: 0; top: 618px;
    width: 86px; height: 28px; background: var(--forest);
    clip-path: polygon(0 0, 100% 0, 100% 100%, 0 100%, 10px 50%);
    color: var(--paper); font-weight: 800; font-size: 17px;
    display: flex; align-items: center; justify-content: center; padding-left: 8px;
  }
</style>
</head>
<body>
  <main class="package-front">
    <svg class="panel-fill" viewBox="0 0 420 660" preserveAspectRatio="none" role="img" aria-label="Leafy forest brand pattern over a deep green upper field and a pale lower field">
      <defs>
        <clipPath id="forest-field">
          <path d="M0 0 H420 V300 C380 292 350 318 310 322 C270 326 250 340 215 352 C180 364 160 378 120 388 C80 398 40 410 0 412 Z"/>
        </clipPath>
        <radialGradient id="leaf-glow-dark">
          <stop offset="0" stop-color="var(--forest-leaf)" stop-opacity="0.9"/>
          <stop offset="1" stop-color="var(--forest-leaf)" stop-opacity="0"/>
        </radialGradient>
        <radialGradient id="leaf-glow-light">
          <stop offset="0" stop-color="var(--paper-leaf)" stop-opacity="1"/>
          <stop offset="1" stop-color="var(--paper-leaf)" stop-opacity="0"/>
        </radialGradient>
      </defs>
      <rect width="420" height="660" fill="var(--paper)"/>
      <g class="paper-pattern">
        <ellipse cx="60" cy="470" rx="90" ry="70" fill="url(#leaf-glow-light)"/>
        <ellipse cx="370" cy="430" rx="90" ry="80" fill="url(#leaf-glow-light)"/>
        <ellipse cx="380" cy="580" rx="80" ry="70" fill="url(#leaf-glow-light)"/>
        <ellipse cx="90" cy="600" rx="70" ry="50" fill="url(#leaf-glow-light)"/>
      </g>
      <g clip-path="url(#forest-field)">
        <rect width="420" height="420" fill="var(--forest)"/>
        <ellipse cx="40" cy="60" rx="90" ry="70" fill="url(#leaf-glow-dark)"/>
        <ellipse cx="380" cy="50" rx="90" ry="70" fill="url(#leaf-glow-dark)"/>
        <ellipse cx="30" cy="250" rx="80" ry="90" fill="url(#leaf-glow-dark)"/>
        <ellipse cx="390" cy="230" rx="70" ry="80" fill="url(#leaf-glow-dark)"/>
        <ellipse cx="110" cy="340" rx="90" ry="60" fill="url(#leaf-glow-dark)"/>
        <ellipse cx="210" cy="150" rx="110" ry="40" fill="url(#leaf-glow-dark)" opacity="0.6"/>
      </g>
    </svg>

    <div class="brand-mark" aria-hidden="true"></div>
    <h1 class="brand-name">Meadow Lark<br>Roasters</h1>

    <div class="quality-seal">
      <svg viewBox="-60 -55 120 110" aria-hidden="true">
        <polygon fill="var(--lime)" transform="scale(1.1,1)" points="52,0 43.2,8.6 48,19.9 36.6,24.5 36.8,36.8 24.5,36.6 19.9,48 8.6,43.2 0,52 -8.6,43.2 -19.9,48 -24.5,36.6 -36.8,36.8 -36.6,24.5 -48,19.9 -43.2,8.6 -52,0 -43.2,-8.6 -48,-19.9 -36.6,-24.5 -36.8,-36.8 -24.5,-36.6 -19.9,-48 -8.6,-43.2 0,-52 8.6,-43.2 19.9,-48 24.5,-36.6 36.8,-36.8 36.6,-24.5 48,-19.9 43.2,-8.6"/>
      </svg>
      <p class="seal-text">Premium<br>Quality</p>
    </div>

    <div class="mascot-art" role="img" aria-label="Illustration of a cheerful tan dog hugging a large steaming cup of coffee"></div>

    <div class="roast-badge">
      <span class="star">★</span>
      <span class="roast-level">Medium</span>
      <span class="roast-word">Roast</span>
      <span class="star">★</span>
    </div>

    <div class="net-weight">16 oz</div>
  </main>
</body>
</html>
```